The new web site for Velmarto srl , Software for production and logistic companies

We need to update our web site.
Velmarto is a software house active in production and logistics solutions.
We would like ho have a new elegant and smart web site.
Right now the site is based on wordpress; it's not mandatory but we would like to be able to add contents, images, news... so, better is we can remain in wordpress.
The actual site is
https://velmarto.it/

Target Market(s)

Productive and logistics companies

Industry/Entity Type

Information Technology

Coding

Coded - Design and coding required

Number of Pages Required

1 page

```html
<!DOCTYPE html>
<html lang="it">
<head>
<meta charset="utf-8">
<title>Velmarto srl</title>
<link href="https://fonts.googleapis.com/css2?family=Montserrat:wght@400;600;700&display=swap" rel="stylesheet">
<style>
:root{
  --brand:#7c1f24;
  --header-bg:#f4f4f4;
  --nav-text:#7a7a7a;
  --white:#ffffff;
}
*{margin:0;padding:0;box-sizing:border-box}
html,body{width:1200px;height:759px;overflow:hidden}
body{font-family:"Montserrat",sans-serif;background:var(--header-bg);position:relative}
.top-bar{position:absolute;left:0;top:0;width:1200px;height:4px;background:var(--brand)}
.site-header{position:absolute;left:0;top:4px;width:1200px;height:155px;background:var(--header-bg)}
.brand{position:absolute;left:151px;top:24px;display:flex;align-items:center;gap:8px}
.brand-mark{width:34px;height:34px;border-radius:50%;background:var(--brand)}
.brand-name{font-weight:700;font-size:25px;color:var(--brand);line-height:1}
.brand-tag{display:block;font-weight:400;font-size:9.5px;color:#888;letter-spacing:.5px;margin-top:3px}
.contacts{position:absolute;top:35px;left:536px;display:flex;align-items:center;gap:16px;font-size:12px;color:var(--brand)}
.contact{display:flex;align-items:center;gap:7px}
.contact svg{width:23px;height:23px}
.social{position:absolute;left:847px;top:35px;display:flex;gap:7px}
.social span{width:23px;height:23px;border-radius:50%;background:var(--brand);display:flex;align-items:center;justify-content:center}
.social svg{width:13px;height:13px}
.search{position:absolute;left:945px;top:31px;width:105px;height:23px;border:1.5px solid var(--brand);border-radius:3px;font-size:8px;color:#999;padding:6px 7px;background:#fff}
.search svg{position:absolute;right:6px;top:5px;width:11px;height:11px}
.main-nav{position:absolute;left:151px;top:113px;width:899px;height:23px;display:flex;align-items:center;justify-content:space-between}
.main-nav a{font-weight:600;font-size:13px;color:var(--nav-text);text-decoration:none;letter-spacing:.5px}
.main-nav .caret::after{content:"";display:inline-block;margin-left:4px;border-left:4px solid transparent;border-right:4px solid transparent;border-top:4px solid var(--nav-text);vertical-align:middle}
.main-nav .cta{background:var(--brand);color:var(--white);padding:5px 23px;border-radius:2px}
.hero{position:absolute;left:0;top:159px;width:1200px;height:600px;
  background:linear-gradient(115deg,#9c8f86 0%,#b8aca3 18%,#a98f7c 30%,#c9c6c3 45%,#e3e2e1 62%,#cfcdcb 78%,#8f8b88 90%,#b3b0ad 100%)}
.hero::after{content:"";position:absolute;inset:0;background:linear-gradient(180deg,rgba(90,80,75,.18),rgba(90,80,75,.05) 50%,rgba(90,80,75,.2))}
.hero > *{z-index:1}
.hero-title{position:absolute;left:147px;top:205px;font-weight:700;font-size:70px;color:var(--white);letter-spacing:1px}
.hero-btn{position:absolute;left:151px;top:327px;width:244px;height:49px;border:2px solid var(--white);border-radius:3px;color:var(--white);font-weight:600;font-size:25px;text-align:center;line-height:44px}
.arrow{position:absolute;top:280px;width:41px;height:41px;border-radius:50%;background:rgba(255,255,255,.85);border:2px solid #555;display:flex;align-items:center;justify-content:center}
.arrow.prev{left:23px}
.arrow.next{left:1136px;border-color:var(--brand)}
.dots{position:absolute;top:566px;left:576px;display:flex;gap:8px}
.dots span{width:11px;height:11px;border-radius:50%;background:var(--white)}
.dots .active{background:var(--brand)}
</style>
</head>
<body>
<div class="top-bar"></div>
<header class="site-header">
  <div class="brand">
    <span class="brand-mark"></span>
    <div><span class="brand-name">Velmarto</span><span class="brand-tag">MES &amp; WMS SPECIALISTS</span></div>
  </div>
  <div class="contacts">
    <span class="contact"><svg viewBox="0 0 24 24"><circle cx="12" cy="12" r="10.5" fill="none" stroke="#7c1f24" stroke-width="2"/><path d="M8 7l2 0 1 3-1.5 1a7 7 0 0 0 3.5 3.5l1-1.5 3 1 0 2c-5 1-10-4-9-9z" fill="#7c1f24"/></svg>+39 0421 508372</span>
    <span class="contact"><svg viewBox="0 0 24 24"><circle cx="12" cy="12" r="10.5" fill="none" stroke="#7c1f24" stroke-width="2"/><rect x="6.5" y="8" width="11" height="8" fill="none" stroke="#7c1f24" stroke-width="1.5"/><path d="M6.5 8l5.5 5 5.5-5" fill="none" stroke="#7c1f24" stroke-width="1.5"/></svg>info@velmarto.it</span>
  </div>
  <div class="social" aria-label="Canali social">
    <span><svg viewBox="0 0 14 14"><circle cx="3" cy="7" r="2" fill="#fff"/><circle cx="11" cy="3" r="2" fill="#fff"/><circle cx="11" cy="11" r="2" fill="#fff"/><path d="M3 7l8-4M3 7l8 4" stroke="#fff" stroke-width="1.3"/></svg></span>
    <span><svg viewBox="0 0 14 14"><path d="M2 3h10v6H6l-3 3V9H2z" fill="#fff"/></svg></span>
    <span><svg viewBox="0 0 14 14"><circle cx="7" cy="7" r="5.5" fill="none" stroke="#fff" stroke-width="1.4"/><path d="M1.5 7h11M7 1.5c-3 3-3 8 0 11M7 1.5c3 3 3 8 0 11" fill="none" stroke="#fff" stroke-width="1.1"/></svg></span>
  </div>
  <div class="search">Cerca nel sito<svg viewBox="0 0 12 12"><circle cx="5" cy="5" r="4" fill="none" stroke="#999" stroke-width="1.2"/><path d="M8 8l3.5 3.5" stroke="#999" stroke-width="1.2"/></svg></div>
  <nav class="main-nav">
    <a class="caret">MES</a><a class="caret">WMS</a><a>RFID</a><a class="caret">RTLS</a><a class="caret">4.0 e 5.0</a><a class="caret">CHI SIAMO</a><a class="caret">REFERENZE</a><a>NEWS</a><a class="cta">CONTATTI</a>
  </nav>
</header>
<section class="hero" role="img" aria-label="Braccio robotico industriale bianco in un laboratorio di produzione">
  <h1 class="hero-title">IMPRESA 4.0</h1>
  <a class="hero-btn">Scopri di piu</a>
  <span class="arrow prev"><svg width="14" height="18" viewBox="0 0 14 18"><path d="M10 2L3 9l7 7" fill="none" stroke="#444" stroke-width="2.5"/></svg></span>
  <span class="arrow next"><svg width="14" height="18" viewBox="0 0 14 18"><path d="M4 2l7 7-7 7" fill="none" stroke="#444" stroke-width="2.5"/></svg></span>
  <div class="dots"><span class="active"></span><span></span><span></span></div>
</section>
</body>
</html>
```